Guaranteed Job - Sleek Sexy Business Card UV Spot

Im looking for a sleek and sexy business card, that resembles elite or VIP status status.
our business is corinvale.example
you can view our products on there, but our main audience for handing out our cards will be for people in the hospitality industry, so it will need to impress high management and CEO of hotels and restaurants, bars, clubs etc...
the card features will have UV spot on both sides, 400gsm stock. standard size.
Artwork should be 86 x 54mm + 2mm bleed = 90 x 58mm
it should have a nice "unique" uv spot pattern that highlights the card, not a repeated pattern, theres no originality there, and it will be disregarded.
The written material will be:
Corin Vale Hospitality College (logo)
Tobin Marsh
Director
Phone: 1300 615 737
Mobile: 0455 817 296
Email: info@corinvale.example
website: www.corinvale.example
I'm looking for originality here, i don't want just a simple stock card, want something that has a wow factor for people.
You will find the logo attached. you may invert the white to black words to suit the background as you please.
thank you and good luck
As a side note, ive received a lot of proposals, im too busy to give feedback to each and every one, so if i havent provided feedback for your design within 24 hours, then consider it not acceptable, and you could resubmit another design.
So far i have not seen any design that stood out for me, they all seem pretty generic. there nothing thats unique, i would figure for the amount that im offering, that people would put some more effort and creativity into the design.
so far over 200 designs submitted, and nothing i have seen looks very original, everything looks like a different variation of the same stuff, i said it very clearly i wanted something unique, the only thing that has come close to it so far is this one
Reason: Ive received alot of design concepts and i have reviewed everyone, but i havent had time to give feedback to every single one, only the ones that have interested me, if i havent responded, its because i havent found it good enough.
so far only a few design have been on par with what ive been looking for, an attractive eye popping design.
heres a few of them,
http://files.pixelbazaar.example/design_img/51736/62418/62418_2840915_51736_image.jpg
http://files.pixelbazaar.example/design_img/51736/68254/68254_2841377_51736_image.jpg
theyre, both unique and original, and eye catching, the only thing theyre missing is the sexyness.
if you still think you have some creativity left in your minds, then throw it on here.
Reason: Sorry guys for the delay, I was in a serious accident and out of commission for the past few months, I'm just slowly recovering now, please bare with me as i try to attend to this project, it may take me awhile as I have other projects that are on standby, I'm not 100% at the moment, so im extending the deadline for 2 weeks right now. Thanks for your patience.
Hospitality

```html
<!DOCTYPE html>
<html lang="en">
<head>
<meta charset="utf-8">
<title>Tobin Marsh – Business Card</title>
<link href="https://fonts.googleapis.com/css2?family=Oswald:wght@500;600&family=Quicksand:wght@400&display=swap" rel="stylesheet">
<style>
  :root {
    --bg: #e4e5e6;
    --card: #22262e;
    --accent: #6a9fd0;
    --uv: #2f3e5a;
    --white: #f2f2f2;
    --grey: #8b8e94;
  }
  * { margin: 0; padding: 0; box-sizing: border-box; }
  html, body {
    width: 1200px; height: 900px; overflow: hidden;
    background: var(--bg);
  }
  .stage {
    position: relative; width: 1200px; height: 900px;
    display: flex; justify-content: center; align-items: center; gap: 120px;
  }
  .card {
    position: relative; width: 390px; height: 620px;
    background: var(--card);
    box-shadow: 0 10px 30px rgba(0,0,0,0.18);
    overflow: hidden;
  }
  /* front */
  .bar-long {
    position: absolute; left: 0; top: 34px; width: 300px; height: 44px;
    background: var(--accent);
  }
  .bar-square {
    position: absolute; left: 316px; top: 44px; width: 44px; height: 40px;
    background: var(--accent);
  }
  .holder { position: absolute; left: 36px; top: 215px; }
  .holder-name {
    font-family: "Oswald", sans-serif; font-weight: 600;
    font-size: 62px; line-height: 1; color: var(--white);
    text-transform: uppercase; letter-spacing: 0.5px;
  }
  .holder-role {
    font-family: "Oswald", sans-serif; font-weight: 600;
    font-size: 30px; line-height: 1; color: var(--grey);
    text-transform: uppercase; margin-top: 2px;
  }
  .contacts { position: absolute; left: 36px; top: 405px; list-style: none; }
  .contact {
    display: flex; align-items: center; gap: 14px; height: 44px;
    font-family: "Quicksand", sans-serif; font-size: 21px; color: var(--white);
  }
  .contact-badge {
    width: 30px; height: 36px; border-radius: 4px;
    background: var(--accent); color: var(--card);
    font-family: "Oswald", sans-serif; font-weight: 600; font-size: 24px;
    display: flex; align-items: center; justify-content: center;
  }
  /* back */
  .uv-mark {
    position: absolute; left: 0; right: 0; top: 120px; text-align: center;
    font-family: "Oswald", sans-serif; font-weight: 600;
    font-size: 92px; line-height: 0.95; color: var(--uv);
    text-transform: uppercase;
  }
  .brand {
    position: absolute; left: 40px; bottom: 56px;
    display: flex; align-items: center; gap: 16px;
  }
  .brand-square { width: 46px; height: 46px; background: var(--accent); }
  .brand-name {
    font-family: "Oswald", sans-serif; font-weight: 500;
    color: var(--white); text-transform: uppercase; line-height: 1.05;
  }
  .brand-name .line-main { display: block; font-size: 32px; }
  .brand-name .line-sub { display: block; font-size: 15px; letter-spacing: 1px; }
</style>
</head>
<body>
  <main class="stage">
    <section class="card card-front">
      <div class="bar-long"></div>
      <div class="bar-square"></div>
      <div class="holder">
        <h1 class="holder-name">Tobin Marsh</h1>
        <p class="holder-role">Director</p>
      </div>
      <ul class="contacts">
        <li class="contact"><span class="contact-badge">P</span>1300 615 737</li>
        <li class="contact"><span class="contact-badge">M</span>0455 817 296</li>
        <li class="contact"><span class="contact-badge">E</span>info@corinvale.example</li>
        <li class="contact"><span class="contact-badge">W</span>www.corinvale.example</li>
      </ul>
    </section>

    <section class="card card-back">
      <div class="uv-mark">Corin<br>Vale</div>
      <div class="brand">
        <span class="brand-square"></span>
        <span class="brand-name">
          <span class="line-main">Corin Vale</span>
          <span class="line-sub">Hospitality College</span>
        </span>
      </div>
    </section>
  </main>
</body>
</html>
```